Home show booth design

We are looking at a home show booth design for our window and door company. We will have some high end doors, windows, patio door and garage door on display. 1 booth is 10x20 and 1 booth is 20x20.

Give me some design ideas and keeping in mind our product on display.

Below is our logo and i would like to keep our branding colors and i want a very attractive and high end setup to stand out from the crowd

Target Market(s)

Home owners and custom home builders

Industry/Entity Type

Windows and doors

Font styles to use
Serif

Colors

Designer to choose colors to be used in the design.

Requirements
Must have
• Back drop, small desk
Nice to have
• Large floating balloon above the booth

```html
<!DOCTYPE html>
<html lang="en">
<head>
<meta charset="utf-8">
<title>Keystone Doors &amp; Windows – Home Show Booth Backdrops</title>
<link rel="stylesheet" href="https://fonts.googleapis.com/css2?family=Anton&family=Poppins:ital,wght@0,400;0,500;0,600;1,800&family=Allura&display=swap">
<style>
  :root{
    --sheet:#d8d8d8;
    --white:#ffffff;
    --orange:#e0661c;
    --orange-deep:#c9551a;
    --brown:#4a4138;
    --ink:#1f1b17;
    --label:#3a3a3a;
  }
  *{box-sizing:border-box;margin:0;padding:0}
  html,body{width:1200px;height:2609px;overflow:hidden}
  body{background:var(--sheet);position:relative;font-family:"Poppins",sans-serif;color:var(--ink)}

  .backdrop{position:absolute;background:var(--white);overflow:hidden;box-shadow:0 6px 18px rgba(0,0,0,.25)}
  .backdrop--tall{left:394px;top:241px;width:468px;height:936px}
  .backdrop--square{left:160px;top:1412px;width:936px;height:936px}

  .size-label{position:absolute;left:0;width:1200px;text-align:center;font-style:italic;font-weight:800;font-size:60px;color:var(--label)}

  .brand{position:absolute;display:flex;align-items:center;font-weight:600;color:var(--orange);line-height:1.15}
  .brand__mark{background:var(--brown);flex:none;border-radius:3px}
  .brand__name{white-space:nowrap}

  .photo{position:absolute}
  .band{position:absolute;left:0;background:linear-gradient(135deg,var(--orange) 0%,var(--orange-deep) 50%,var(--orange) 100%)}
  .footer-bar{position:absolute;left:0;background:var(--brown)}

  .pill{position:absolute;transform:translate(-50%,-50%);background:var(--brown);color:var(--white);border:3px solid var(--white);border-radius:40px;font-weight:400;text-align:center;white-space:nowrap}
  .thumb{position:absolute;border:2px solid var(--white);border-radius:6px;box-shadow:0 2px 6px rgba(0,0,0,.25)}

  .intro{position:absolute;font-weight:400;color:var(--ink);white-space:nowrap;line-height:1}
  .script{position:absolute;font-family:"Allura",cursive;color:var(--orange);white-space:nowrap;line-height:1}
  .headline{position:absolute;font-family:"Anton",sans-serif;font-weight:400;color:var(--brown);white-space:nowrap;line-height:1.02}

  .url{position:absolute;font-weight:400;color:var(--ink);white-space:nowrap;text-align:center}
  .url b{color:var(--orange);font-weight:600}
</style>
</head>
<body>

<!-- 10x20 backdrop -->
<section class="backdrop backdrop--tall" aria-label="10x20 booth backdrop">
  <div class="photo" role="img" aria-label="Two-storey stone and white-siding family home under a pale sky, with lawn, hedges and trees"
       style="left:0;top:150px;width:468px;height:384px;background:
         linear-gradient(180deg,rgba(255,255,255,1) 0%,rgba(255,255,255,0) 22%),
         linear-gradient(180deg,#e7eef1 0%,#b9d0da 30%,#9fb7bf 42%,#8c7c6a 52%,#7a6757 64%,#5e4c40 74%,#3e5a2c 84%,#6a8c3e 100%)"></div>

  <div class="brand" style="left:136px;top:56px;gap:10px;font-size:19px">
    <span class="brand__mark" style="width:68px;height:68px"></span>
    <span class="brand__name">Keystone<br>Doors &amp; Windows</span>
  </div>

  <p class="intro" style="left:101px;top:173px;font-size:23px">Elevate Your Home</p>
  <p class="script" style="left:312px;top:164px;font-size:50px">with</p>
  <h1 class="headline" style="left:0;width:468px;text-align:center;top:206px;font-size:50px">Keystone Doors<br>&amp; Windows</h1>

  <div class="band" style="top:532px;width:468px;height:256px;border-top:3px solid var(--white)"></div>

  <span class="pill" style="left:234px;top:535px;width:276px;height:54px;font-size:29px;line-height:48px">High end doors</span>
  <div class="thumb" role="img" aria-label="Grey front door with sidelight and porch column" style="left:55px;top:572px;width:117px;height:95px;background:linear-gradient(90deg,#cfd3d6 0%,#5a6066 25%,#3c4247 45%,#eef0f1 62%,#4f6a3a 80%,#6d8a4a 100%)"></div>
  <div class="thumb" role="img" aria-label="White front door set in warm wood cladding" style="left:176px;top:572px;width:117px;height:95px;background:linear-gradient(90deg,#e9e6e0 0%,#9a5a36 22%,#b8764a 34%,#f5f3ef 45%,#f5f3ef 62%,#a8623b 75%,#e4e2de 100%)"></div>
  <div class="thumb" role="img" aria-label="Modern double entry door on a stone facade" style="left:297px;top:572px;width:117px;height:95px;background:linear-gradient(180deg,#e4e8e7 0%,#b3a587 30%,#8b7a60 48%,#2f2b27 62%,#3a342e 78%,#6f8a4a 100%)"></div>

  <span class="pill" style="left:234px;top:706px;width:188px;height:54px;font-size:29px;line-height:48px">Windows</span>
  <div class="thumb" role="img" aria-label="Bright room with tall casement windows and potted plants" style="left:55px;top:742px;width:117px;height:95px;background:linear-gradient(90deg,#f3f3f1 0%,#b9cfa6 30%,#8fb36f 50%,#dfe7d6 70%,#6b5447 100%)"></div>
  <div class="thumb" role="img" aria-label="Living room with arched windows and brick accents" style="left:176px;top:742px;width:117px;height:95px;background:linear-gradient(180deg,#a9573a 0%,#c9b4a2 25%,#eee9e1 50%,#f4f1ec 80%,#d9cfc2 100%)"></div>
  <div class="thumb" role="img" aria-label="Sunroom lounge with a full wall of windows" style="left:297px;top:742px;width:117px;height:95px;background:linear-gradient(180deg,#f4f6f7 0%,#dbe3e6 40%,#8b7c66 65%,#2f4b63 82%,#243a4e 100%)"></div>

  <p class="url" style="left:0;width:468px;top:854px;font-size:28px">www.<b>keystonedoors</b>.org</p>
  <div class="footer-bar" style="top:924px;width:468px;height:12px"></div>
</section>
<p class="size-label" style="top:1200px">10x20</p>

<!-- 20x20 backdrop -->
<section class="backdrop backdrop--square" aria-label="20x20 booth backdrop">
  <div class="photo" role="img" aria-label="Company warehouse with blue metal cladding, pickup trucks and a box truck parked in front"
       style="left:0;top:120px;width:936px;height:455px;background:
         linear-gradient(180deg,rgba(255,255,255,1) 0%,rgba(255,255,255,0) 20%),
         linear-gradient(180deg,#eef3f7 0%,#c7d9e8 18%,#7fa9cf 30%,#5b90c0 44%,#4a7fae 56%,#1f3446 66%,#dfe3e6 74%,#b4bcc2 84%,#8ea06a 92%,#7f9a52 100%)"></div>

  <div class="brand" style="left:60px;top:60px;flex-direction:column;gap:12px;font-size:22px;text-align:center;width:176px">
    <span class="brand__mark" style="width:80px;height:80px"></span>
    <span class="brand__name">Keystone<br>Doors &amp; Windows</span>
  </div>

  <p class="intro" style="left:263px;top:77px;font-size:37px">Elevate Your Home</p>
  <p class="script" style="left:624px;top:62px;font-size:68px">with</p>
  <h1 class="headline" style="left:261px;top:120px;font-size:54px">Keystone Doors &amp; Windows</h1>

  <div class="band" style="top:572px;width:936px;height:276px;border-top:3px solid var(--white)"></div>

  <span class="pill" style="left:253px;top:578px;width:210px;height:54px;font-size:30px;line-height:48px">Patio door</span>
  <span class="pill" style="left:686px;top:574px;width:232px;height:54px;font-size:30px;line-height:48px">Garage door</span>

  <div class="thumb" role="img" aria-label="Living room opening onto a sliding patio door" style="left:78px;top:631px;width:167px;height:157px;background:linear-gradient(180deg,#ecebe8 0%,#c9c6c0 30%,#7a766f 50%,#a9a39a 65%,#6b5a52 82%,#5c4f49 100%)"></div>
  <div class="thumb" role="img" aria-label="Sliding patio door in a bright kitchen" style="left:257px;top:631px;width:167px;height:157px;background:linear-gradient(90deg,#3b3b3b 0%,#b9c79c 25%,#e4ead6 45%,#3f3f3f 55%,#f3eee6 70%,#e2d3bd 100%)"></div>
  <div class="thumb" role="img" aria-label="Bungalow with a grey garage door at dusk" style="left:513px;top:631px;width:167px;height:157px;background:linear-gradient(180deg,#2f5f8c 0%,#7fa6c6 35%,#b9cfdf 50%,#8a766b 68%,#5d5856 85%,#3f3f3f 100%)"></div>
  <div class="thumb" role="img" aria-label="Stone two-storey home with a double garage door" style="left:692px;top:631px;width:167px;height:157px;background:linear-gradient(180deg,#6f7888 0%,#c8c9cc 35%,#9b907e 55%,#6f6657 72%,#5f8a3e 88%,#4f7632 100%)"></div>

  <div class="footer-bar" style="top:846px;width:936px;height:90px"></div>
  <p class="url" style="left:154px;top:817px;width:628px;height:58px;line-height:56px;background:var(--white);border-radius:30px;font-size:37px;letter-spacing:5px">www.<b>keystonedoors</b>.org</p>
</section>
<p class="size-label" style="top:2376px">20x20</p>

</body>
</html>
```